Modern and Vibrant Car Wash Website

In Summary: A website using our Menus for Exterior and Full Service Car Washes: Meadowlark, tidewater car wash, Vireo and Copperleaf Express Car Wash websites (link attached below are good references for the type of cartoony fun design).

I will add our flyer, and menus, and some other graphics as a visual reference. Will over time add the files (AI and SVG so you can use them).

Car wash front page should be nice and clean. I have lots of videos and photos we can use throughout the wash. Would like a video on the landing page.

Our shop section can remain blank as my POS developers will create a hyperlink to it.

Main easy to use functions should be the Car Wash services, their price and full service ones as well. Allow customers to see, book if needed etc.

Please note I have the website on PLOM.

I have attached a general pdf as well for some more info.

https://meadowlarkgleamwash.ca/
https://tidewatercarwash.ca/
https://marblecarwash.com/
https://vireowash.com/
https://plainpagebuilder.com/carwash-website-design/
https://copperleafexpresscarwash.com/

```html
<!DOCTYPE html>
<html lang="en">
<head>
<meta charset="utf-8">
<title>Gloss &amp; Go — Car Wash</title>
<link rel="stylesheet" href="https://fonts.googleapis.com/css2?family=Barlow:wght@400;500;600;700&family=Barlow+Semi+Condensed:wght@400;500;600;700&display=swap">
<style>
:root{
  --blue:#0a6fbf;
  --blue-light:#c9e2f7;
  --yellow:#fccb2a;
  --ink:#111111;
  --text:#3b3b3b;
  --muted:#8a8f96;
  --page:#f4f6f8;
  --band:#e4e4e4;
  --line:#d9dde2;
  --black:#000000;
  --panel:#1e1e1e;
  --white:#ffffff;
}
*{box-sizing:border-box;margin:0;padding:0}
html,body{width:1200px;height:4165px;overflow:hidden}
body{position:relative;background:var(--page);font-family:"Barlow Semi Condensed","Barlow",sans-serif;color:var(--text)}
.abs{position:absolute}
h1,h2,h3{font-family:"Barlow",sans-serif;font-weight:700;color:var(--ink)}
.accent{color:var(--yellow)}
.btn{position:absolute;display:flex;align-items:center;justify-content:center;border-radius:8px;font-size:15px;text-decoration:none;z-index:2}
.btn-blue{background:var(--blue);color:var(--white)}
.btn-yellow{background:var(--yellow);color:var(--ink)}

/* header */
.site-header{position:absolute;left:0;top:0;width:1200px;height:74px;background:var(--white);z-index:3}
.brand{position:absolute;left:80px;top:21px;display:flex;align-items:center;gap:8px;font-family:"Barlow",sans-serif;font-weight:700;font-size:24px;color:var(--blue)}
.brand-dot{width:26px;height:26px;border-radius:50%;background:var(--yellow)}
.main-nav a{position:absolute;top:27px;font-size:15px;color:var(--ink);text-decoration:none}
.main-nav a.active{color:var(--blue)}

/* hero */
.hero{position:absolute;left:0;top:74px;width:1200px;height:760px}
.hero-band,.hero-art{position:absolute;left:0;top:0}
.hero-title{position:absolute;left:0;top:78px;width:1200px;text-align:center;font-size:60px;line-height:66px;z-index:2}

/* services */
.section-title{position:absolute;left:0;width:1200px;text-align:center;font-size:52px}
.service-card{position:absolute;top:1024px;width:505px;height:626px;border:1px solid var(--line);border-radius:10px;background:var(--page)}
.service-badge{position:absolute;left:145px;top:-83px;width:214px;height:214px;border-radius:50%;background:var(--yellow);display:flex;align-items:center;justify-content:center}
.service-name{position:absolute;left:0;width:100%;text-align:center;font-size:26px;font-weight:600;font-family:"Barlow",sans-serif;color:var(--ink)}
.service-price{position:absolute;left:0;width:100%;text-align:center;font-size:44px;font-weight:700;font-family:"Barlow",sans-serif;color:var(--blue)}
.feature-list{position:absolute;left:56px;top:306px;list-style:none}
.feature-list li{display:flex;align-items:center;gap:22px;height:40.7px;font-size:15px;color:var(--ink)}
.service-card .btn{left:179px;top:602px;width:146px;height:42px}

/* about */
.about-title{position:absolute;left:79px;top:1762px;font-size:52px}
.about-copy{position:absolute;left:79px;top:1840px;width:475px;font-family:"Barlow",sans-serif;font-size:14.5px;line-height:31.5px;color:var(--text)}
.about-blob{position:absolute;left:700px;top:1770px;width:410px;height:350px;border-radius:48% 52% 40% 60%/50% 45% 55% 50%;background:var(--blue-light);transform:rotate(-18deg)}
.about-photo{position:absolute;left:653px;top:1811px;width:409px;height:270px;border-radius:90px;background:radial-gradient(ellipse at 50% 60%,#6f8aa3 0%,#2f3d4a 55%,#161c22 100%)}

/* testimonials */
.reviews{position:absolute;left:0;top:2235px;width:1200px;height:748px;background:var(--band)}
.reviews-title{position:absolute;left:0;top:70px;width:1200px;text-align:center;font-size:50px;line-height:64px}
.review-card{position:absolute;top:266px;width:322px;height:350px;border:1px solid #cfcfcf;border-radius:10px;background:var(--band)}
.review-card.featured{background:var(--white);border:none;box-shadow:0 6px 20px rgba(0,0,0,.15)}
.review-head{position:absolute;left:16px;top:20px;font-size:19px;color:var(--ink)}
.review-quote{position:absolute;left:16px;top:62px;width:26px;height:26px;border-radius:50%;background:#fbe7a6;color:var(--yellow);font-family:"Barlow",sans-serif;font-weight:700;font-size:26px;line-height:34px;text-align:center}
.review-text{position:absolute;left:56px;top:62px;width:252px;font-family:"Barlow",sans-serif;font-size:12.5px;line-height:25.5px;color:var(--text)}
.review-rule{position:absolute;left:54px;top:229px;width:250px;height:1px;background:#c9c9c9}
.avatar{position:absolute;left:64px;top:247px;width:42px;height:42px;border-radius:50%;background:linear-gradient(#b8896a,#4a3a30)}
.reviewer{position:absolute;left:124px;top:254px;font-size:13px;font-weight:600;color:var(--ink)}
.stars{position:absolute;left:122px;top:276px;font-size:14px;letter-spacing:2px;color:var(--yellow)}
.stars .off{color:#cfcfcf}
.dots{position:absolute;left:580px;top:685px;display:flex;gap:3px}
.dots span{width:11px;height:3px;background:var(--yellow)}
.dots span.on{background:#555}

/* contact */
.field{position:absolute;height:47px;border:2px solid var(--line);border-radius:10px;background:var(--page);display:flex;align-items:center;padding-left:18px;font-size:13px;color:var(--muted)}
.field svg{margin-right:10px}
.field .sep{width:1px;height:18px;background:var(--muted);margin-right:10px}
.field.message{align-items:flex-start;padding-top:14px}

/* footer */
.site-footer{position:absolute;left:0;top:3582px;width:1200px;height:583px;background:var(--black);color:var(--white)}
.info-box{position:absolute;top:71px;width:339px;height:76px;border-radius:10px;background:var(--panel);display:flex;align-items:center;padding-left:14px;gap:18px}
.info-box strong{display:block;font-weight:500;font-size:16px}
.info-box span{font-size:12.5px}
.footer-brand{position:absolute;left:0;top:212px;width:1200px;display:flex;justify-content:center;align-items:center;gap:12px;font-family:"Barlow",sans-serif;font-weight:700;font-size:44px;color:var(--yellow)}
.footer-brand i{width:36px;height:36px;border-radius:50%;background:var(--blue);display:block}
.socials{position:absolute;left:500px;top:346px;display:flex;gap:18px}
.socials span{width:32px;height:30px;border:2.5px solid var(--blue);border-radius:7px}
.socials span.alt{border-color:var(--yellow)}
.footer-nav{position:absolute;left:0;top:415px;width:1200px;display:flex;justify-content:center;gap:40px;font-size:13px}
.footer-nav a{color:var(--white);text-decoration:none}
.footer-rule{position:absolute;left:79px;top:490px;width:1042px;height:1px;background:#555}
.copyright{position:absolute;left:0;top:512px;width:1200px;text-align:center;font-size:12.5px}
</style>
</head>
<body>

<header class="site-header">
  <div class="brand"><span class="brand-dot"></span>Gloss &amp; Go</div>
  <nav class="main-nav">
    <a class="active" style="left:505px">Home</a>
    <a style="left:580px">About Us</a>
    <a style="left:676px">Services</a>
    <a style="left:770px">Prices</a>
    <a style="left:851px">Testimonial</a>
  </nav>
  <a class="btn btn-yellow" style="left:1003px;top:19px;width:116px;height:36px;font-size:14px">Contact Us</a>
</header>

<section class="hero">
  <svg class="hero-band" width="1200" height="760" viewBox="0 0 1200 760" aria-hidden="true">
    <path d="M0 0H1200V680C1080 660 960 640 760 650C520 662 320 740 160 740C90 740 40 730 0 722Z" fill="#0a6fbf"/>
  </svg>
  <svg class="hero-art" width="1200" height="760" viewBox="0 0 1200 760" role="img" aria-label="Cartoon attendant spraying foam onto an orange car">
    <defs>
      <clipPath id="heroWave">
        <path d="M0 0H1200V680C1080 660 960 640 760 650C520 662 320 740 160 740C90 740 40 730 0 722Z"/>
      </clipPath>
      <linearGradient id="heroArtFill" x1="0" y1="0" x2="1" y2="0.4">
        <stop offset="0" stop-color="#2fa765"/>
        <stop offset="0.3" stop-color="#d99a2e"/>
        <stop offset="1" stop-color="#c8861f"/>
      </linearGradient>
    </defs>
    <g clip-path="url(#heroWave)">
      <rect x="60" y="300" width="1180" height="420" rx="60" fill="url(#heroArtFill)" opacity="0.9"/>
    </g>
  </svg>
  <h1 class="hero-title">Professional washing and<br><span class="accent">cleaning of your car</span></h1>
  <a class="btn btn-yellow" style="left:524px;top:238px;width:147px;height:44px;font-size:16px">Book Now</a>
</section>

<h2 class="section-title" style="top:882px"><span class="accent">Our</span> Services</h2>

<article class="service-card" style="left:79px">
  <div class="service-badge">
    <svg width="120" height="90" viewBox="0 0 120 90" fill="none" stroke="#0a6fbf" stroke-width="8" stroke-linejoin="round"><path d="M18 48 30 20h60l12 28v30H18Z"/><path d="M18 78v8M102 78v8" stroke-linecap="round"/><circle cx="36" cy="60" r="5" fill="#0a6fbf"/><circle cx="84" cy="60" r="5" fill="#0a6fbf"/><path d="M34 42h52"/></svg>
  </div>
  <h3 class="service-name" style="top:214px">Complete Clean</h3>
  <div class="service-price" style="top:246px">$54.99</div>
  <ul class="feature-list">
    <li><svg width="20" height="20" viewBox="0 0 20 20"><path d="M10 0 12 8 20 10 12 12 10 20 8 12 0 10 8 8Z" fill="#fccb2a"/></svg>Full Exterior Hand Dry</li>
    <li><svg width="20" height="20" viewBox="0 0 20 20"><path d="M10 0 12 8 20 10 12 12 10 20 8 12 0 10 8 8Z" fill="#fccb2a"/></svg>Thoourgh Interior Vacuum</li>
    <li><svg width="20" height="20" viewBox="0 0 20 20"><path d="M10 0 12 8 20 10 12 12 10 20 8 12 0 10 8 8Z" fill="#fccb2a"/></svg>Rubber and Carpet Mat-Refresh</li>
    <li><svg width="20" height="20" viewBox="0 0 20 20"><path d="M10 0 12 8 20 10 12 12 10 20 8 12 0 10 8 8Z" fill="#fccb2a"/></svg>Interior Steam Clean and disinfect</li>
    <li><svg width="20" height="20" viewBox="0 0 20 20"><path d="M10 0 12 8 20 10 12 12 10 20 8 12 0 10 8 8Z" fill="#fccb2a"/></svg>Rims Steam-Cleaned and Wiped</li>
    <li><svg width="20" height="20" viewBox="0 0 20 20"><path d="M10 0 12 8 20 10 12 12 10 20 8 12 0 10 8 8Z" fill="#fccb2a"/></svg>Interior Glass and Mirror Clean</li>
    <li><svg width="20" height="20" viewBox="0 0 20 20"><path d="M10 0 12 8 20 10 12 12 10 20 8 12 0 10 8 8Z" fill="#fccb2a"/></svg>Hand Applied</li>
  </ul>
  <a class="btn btn-blue">View All Sevices</a>
</article>

<article class="service-card" style="left:615px">
  <div class="service-badge">
    <svg width="120" height="110" viewBox="0 0 120 110" fill="none" stroke="#0a6fbf" stroke-width="8" stroke-linejoin="round"><circle cx="40" cy="22" r="9" fill="#0a6fbf"/><circle cx="70" cy="14" r="9" fill="#0a6fbf"/><circle cx="88" cy="30" r="10" fill="#0a6fbf"/><path d="M18 66 30 40h60l12 26v30H18Z"/><circle cx="36" cy="78" r="5" fill="#0a6fbf"/><circle cx="84" cy="78" r="5" fill="#0a6fbf"/></svg>
  </div>
  <h3 class="service-name" style="top:188px">Exepress Clean</h3>
  <div class="service-price" style="top:220px">$39.99</div>
  <ul class="feature-list">
    <li><svg width="20" height="20" viewBox="0 0 20 20"><path d="M10 0 12 8 20 10 12 12 10 20 8 12 0 10 8 8Z" fill="#fccb2a"/></svg>Full Exterior Hand Dry</li>
    <li><svg width="20" height="20" viewBox="0 0 20 20"><path d="M10 0 12 8 20 10 12 12 10 20 8 12 0 10 8 8Z" fill="#fccb2a"/></svg>Thoourgh Interior Vacuum</li>
    <li><svg width="20" height="20" viewBox="0 0 20 20"><path d="M10 0 12 8 20 10 12 12 10 20 8 12 0 10 8 8Z" fill="#fccb2a"/></svg>Rubber and Carpet Mat-Refresh</li>
    <li><svg width="20" height="20" viewBox="0 0 20 20"><path d="M10 0 12 8 20 10 12 12 10 20 8 12 0 10 8 8Z" fill="#fccb2a"/></svg>Interior Steam Clean and disinfect</li>
    <li><svg width="20" height="20" viewBox="0 0 20 20"><path d="M10 0 12 8 20 10 12 12 10 20 8 12 0 10 8 8Z" fill="#fccb2a"/></svg>Rims Steam-Cleaned and Wiped</li>
    <li><svg width="20" height="20" viewBox="0 0 20 20"><path d="M10 0 12 8 20 10 12 12 10 20 8 12 0 10 8 8Z" fill="#fccb2a"/></svg>Interior Glass and Mirror Clean</li>
    <li><svg width="20" height="20" viewBox="0 0 20 20"><path d="M10 0 12 8 20 10 12 12 10 20 8 12 0 10 8 8Z" fill="#fccb2a"/></svg>Hand Applied</li>
  </ul>
  <a class="btn btn-blue">View All Sevices</a>
</article>

<h2 class="about-title"><span class="accent">Who</span> we are</h2>
<p class="about-copy">Over the past 6 years we cleaned over 34,000 cars, saved over 8,9 million liters of water from being used in car washing and employed 50 youth. Our legacy is in the youth that gained work and life skills, grew their confidence and have moved on to bigger.<br>Over the past 6 years we cleaned over 34,000 cars, saved over 8,9 million liters of water from being used in car washing and employed 50 youth. Our legacy is in the youth that gained work and life skills, grew their confidence and have moved on to bigger.</p>
<a class="btn btn-blue" style="left:79px;top:2110px;width:144px;height:42px">Read More</a>
<div class="about-blob"></div>
<div class="about-photo" role="img" aria-label="Photo of a foam-covered car in a wash bay"></div>

<section class="reviews">
  <h2 class="reviews-title"><span style="color:var(--blue)">What our</span><br>customers says</h2>

  <div class="review-card" style="left:79px">
    <div class="review-head">Ameging Expireance</div>
    <div class="review-quote">“</div>
    <p class="review-text">Over the past 6 years we cleaned over 34,000 cars, saved over 8.9 million liters of water from being used in car washing and employed 50 youth</p>
    <div class="review-rule"></div>
    <div class="avatar" role="img" aria-label="Customer portrait"></div>
    <div class="reviewer">Rowan T</div>
    <div class="stars">★★★★★</div>
  </div>

  <div class="review-card featured" style="left:441px">
    <div class="review-head">Ameging Expireance</div>
    <div class="review-quote">“</div>
    <p class="review-text">Over the past 6 years we cleaned over 34,000 cars, saved over 8.9 million liters of water from being used in car washing and employed 50 youth</p>
    <div class="review-rule"></div>
    <div class="avatar" role="img" aria-label="Customer portrait"></div>
    <div class="reviewer">Rowan T</div>
    <div class="stars">★★★★★<span class="off">★</span></div>
  </div>

  <div class="review-card" style="left:800px">
    <div class="review-head">Ameging Expireance</div>
    <div class="review-quote">“</div>
    <p class="review-text">Over the past 6 years we cleaned over 34,000 cars, saved over 8.9 million liters of water from being used in car washing and employed 50 youth</p>
    <div class="review-rule"></div>
    <div class="avatar" role="img" aria-label="Customer portrait"></div>
    <div class="reviewer">Rowan T</div>
    <div class="stars">★★★★★</div>
  </div>

  <div class="dots"><span></span><span class="on"></span><span></span></div>
</section>

<h2 class="section-title" style="top:3064px"><span class="accent">Get</span> in touch</h2>

<div class="field" style="left:260px;top:3181px;width:329px">
  <svg width="14" height="14" viewBox="0 0 14 14" fill="none" stroke="#555" stroke-width="1.3"><circle cx="7" cy="4.5" r="3"/><path d="M1.5 13c0-3 2.5-4.5 5.5-4.5s5.5 1.5 5.5 4.5"/></svg><i class="sep"></i>First Name</div>
<div class="field" style="left:610px;top:3181px;width:330px">
  <svg width="14" height="14" viewBox="0 0 14 14" fill="none" stroke="#555" stroke-width="1.3"><circle cx="7" cy="4.5" r="3"/><path d="M1.5 13c0-3 2.5-4.5 5.5-4.5s5.5 1.5 5.5 4.5"/></svg><i class="sep"></i>Last Name</div>
<div class="field" style="left:260px;top:3249px;width:329px">
  <svg width="15" height="12" viewBox="0 0 15 12" fill="none" stroke="#555" stroke-width="1.3"><rect x="1" y="1" width="13" height="10" rx="1.5"/><path d="m1 2 6.5 5L14 2"/></svg><i class="sep"></i>E mail</div>
<div class="field" style="left:610px;top:3249px;width:330px">
  <svg width="14" height="14" viewBox="0 0 14 14" fill="none" stroke="#555" stroke-width="1.3"><path d="M3 1 5 4 3.8 5.5a8 8 0 0 0 4.7 4.7L10 9l3 2-1.2 2C6 13 1 8 1 2.2Z"/></svg><i class="sep"></i>Phone Number</div>
<div class="field message" style="left:260px;top:3317px;width:680px;height:88px">
  <svg width="14" height="13" viewBox="0 0 14 13" fill="none" stroke="#555" stroke-width="1.3"><path d="M1.5 1.5h11v8h-7l-3 2.5v-2.5h-1Z"/></svg><i class="sep"></i>Massage</div>
<a class="btn btn-blue" style="left:477px;top:3439px;width:273px;height:41px">Submit Now</a>

<footer class="site-footer">
  <div class="info-box" style="left:81px">
    <svg width="30" height="34" viewBox="0 0 30 34" fill="none" stroke="#fff" stroke-width="2"><path d="M15 32S4 20 4 12a11 11 0 0 1 22 0c0 8-11 20-11 20Z"/><circle cx="15" cy="12" r="4"/></svg>
    <div><strong>Address</strong><span>482 Alder Row, Fairhaven, ST 00000</span></div>
  </div>
  <div class="info-box" style="left:430px">
    <svg width="32" height="32" viewBox="0 0 32 32" fill="none" stroke="#fff" stroke-width="2"><path d="M7 3 12 10 9.5 13a18 18 0 0 0 9.5 9.5L22 20l7 5-2.5 4C14 29 3 18 3 5.5Z"/><path d="M19 4a10 10 0 0 1 9 9M19 9a5 5 0 0 1 4 4"/></svg>
    <div><strong>Call Us</strong><span>0 (555) 014-22-07</span></div>
  </div>
  <div class="info-box" style="left:780px">
    <svg width="34" height="26" viewBox="0 0 34 26" fill="none" stroke="#fff" stroke-width="2"><rect x="2" y="2" width="30" height="22" rx="2"/><path d="m2 3 15 12L32 3M2 23l11-10M32 23 21 13"/></svg>
    <div><strong>E mail</strong><span>hello@glossandgo.example</span></div>
  </div>

  <div class="footer-brand"><i></i>Gloss &amp; Go</div>

  <div class="socials"><span></span><span class="alt"></span><span></span><span></span></div>

  <nav class="footer-nav">
    <a>Home</a><a>About Us</a><a>Services</a><a>Prices</a><a>Testimonial</a>
  </nav>
  <div class="footer-rule"></div>
  <p class="copyright">©Copyright 2025 Gloss &amp; Go. All Rights Reserved - 2025 - Purchase</p>
</footer>

</body>
</html>
```